Breezeway Comfort business cards design

Need a business card design for a Heating and Air Conditioning business. I need these items included.
Business name: Breezeway Comfort
Owner: Marcus Holloway
License # 2748519
Phone number # 555-382-4067
Email: breezewaycomfortair@mailnest.example
Sales
Service
Installation
Maintenance

Heating and Air Conditioning

Requirements
Must have
• Company name , license number , phone number , email

```html
<!DOCTYPE html>
<html lang="en">
<head>
<meta charset="UTF-8">
<title>Breezeway Comfort – Business Cards</title>
<link rel="stylesheet" href="https://fonts.googleapis.com/css2?family=Montserrat:wght@400;500;800&display=swap">
<style>
  :root {
    --page-bg: #2a2a2e;
    --card-white: #f7f7f7;
    --card-black: #1b1b1d;
    --pattern-tone: #242427;
    --brand-blue: #1f3f9e;
    --brand-orange: #f26a2e;
    --ink: #2b2b2b;
    --faint-mark: #ececec;
  }
  * { margin: 0; padding: 0; box-sizing: border-box; }
  html, body { width: 1200px; height: 947px; overflow: hidden; }
  body {
    background: var(--page-bg);
    font-family: "Montserrat", sans-serif;
    position: relative;
  }
  .card {
    position: absolute;
    left: 250px;
    width: 700px;
    height: 400px;
    border-radius: 22px;
    overflow: hidden;
  }
  .card--back { top: 50px; background: var(--card-black); }
  .card--front { top: 497px; background: var(--card-white); }

  .back-pattern {
    position: absolute; inset: 0;
    background: radial-gradient(circle at 50% 50%, var(--pattern-tone), var(--card-black) 75%);
  }
  .back-brand {
    position: absolute; left: 0; right: 0; top: 50%;
    transform: translateY(-50%);
    display: flex; align-items: center; justify-content: center; gap: 14px;
  }
  .brand-dot {
    width: 26px; height: 26px; border-radius: 50%;
    background: var(--brand-orange);
  }
  .brand-name {
    font-weight: 800;
    font-size: 30px;
    letter-spacing: 2px;
    text-transform: uppercase;
    color: var(--brand-blue);
  }

  .front-mark {
    position: absolute;
    right: -90px; top: -60px;
    width: 420px; height: 420px;
    border-radius: 50%;
    background: var(--faint-mark);
  }
  .front-content {
    position: absolute; left: 50px; top: 42px;
    color: var(--ink);
  }
  .front-brand { display: flex; align-items: center; gap: 12px; margin-bottom: 26px; }
  .front-brand .brand-name { font-size: 34px; }
  .owner-name {
    font-weight: 800; font-size: 30px;
    color: var(--brand-blue); text-transform: uppercase;
    letter-spacing: 0.5px; line-height: 1.1;
  }
  .owner-title { font-size: 17px; letter-spacing: 1px; margin-top: 4px; }
  .license { font-size: 17px; margin-top: 2px; }
  .divider { width: 14px; height: 2px; background: var(--ink); margin: 14px 0; }
  .contact-row { display: flex; align-items: center; gap: 12px; font-size: 17px; line-height: 1.5; }
  .contact-row svg { width: 14px; height: 14px; flex: none; }
  .services { font-size: 17px; line-height: 1.5; }
</style>
</head>
<body>
  <section class="card card--back" aria-label="Card back">
    <div class="back-pattern" role="img" aria-label="Embossed repeating brand pattern in dark tones"></div>
    <div class="back-brand">
      <span class="brand-dot"></span>
      <span class="brand-name">Breezeway Comfort</span>
    </div>
  </section>

  <section class="card card--front" aria-label="Card front">
    <div class="front-mark" role="img" aria-label="Faint large brand decoration"></div>
    <div class="front-content">
      <div class="front-brand">
        <span class="brand-name">Breezeway Comfort</span>
      </div>
      <div class="owner-name">Marcus Holloway</div>
      <div class="owner-title">OWNER</div>
      <div class="license">License # 2748519</div>
      <div class="divider"></div>
      <div class="contact-row">
        <svg viewBox="0 0 24 24" aria-hidden="true"><path fill="var(--brand-orange)" d="M6.6 10.8a15.1 15.1 0 0 0 6.6 6.6l2.2-2.2a1 1 0 0 1 1-.25 11.4 11.4 0 0 0 3.6.57 1 1 0 0 1 1 1V20a1 1 0 0 1-1 1A17 17 0 0 1 3 4a1 1 0 0 1 1-1h3.5a1 1 0 0 1 1 1c0 1.25.2 2.45.57 3.57a1 1 0 0 1-.25 1z"/></svg>
        <span>555-382-4067</span>
      </div>
      <div class="contact-row">
        <svg viewBox="0 0 24 24" aria-hidden="true"><rect x="2" y="5" width="20" height="14" rx="2" fill="var(--brand-orange)"/><path d="M2 7l10 6 10-6" fill="none" stroke="#fff" stroke-width="2"/></svg>
        <span>breezewaycomfortair@mailnest.example</span>
      </div>
      <div class="divider"></div>
      <div class="services">Sales | Service<br>Installation | Maintenance</div>
    </div>
  </section>
</body>
</html>
```